Floor Inspections and Consulting

We provide inspections and consulting services on various floor coverings, e.g. carpet, hardwood, etc. We also do expert witness work for attorneys due to floor covering failures. We current have a logo, just need it incorporated into a new design. I have examples of cards I have found on the internet that capture my attention and make a statement. I have included our original business card, which in my opinion is terrible, but it does have our logo on it.

```html
<!DOCTYPE html>
<html lang="en">
<head>
<meta charset="utf-8">
<title>Keystone Floor Review – Business Cards</title>
<link href="https://fonts.googleapis.com/css2?family=Open+Sans:wght@400;600;700&display=swap" rel="stylesheet">
<style>
  :root {
    --backdrop: #3d3d3e;
    --card-dark: #2b2b2c;
    --panel-light: #ececec;
    --brand-blue: #1e8bbf;
    --brand-blue-deep: #176f99;
    --ink: #1f1f1f;
    --white: #ffffff;
    --emboss: #3e3e40;
  }
  * { box-sizing: border-box; margin: 0; padding: 0; }
  html, body {
    width: 1200px; height: 1021px; overflow: hidden;
    background: var(--backdrop);
    font-family: "Open Sans", Arial, sans-serif;
  }
  .card {
    position: absolute; left: 250px;
    width: 700px; height: 400px;
    background: var(--card-dark);
    box-shadow: 0 14px 30px rgba(0,0,0,.35);
    overflow: hidden;
  }
  .card--back { top: 80px; }
  .card--front { top: 540px; }

  /* back */
  .back-accents { position: absolute; inset: 0; }
  .back-brand {
    position: absolute; left: 0; right: 0; top: 130px;
    text-align: center; color: var(--emboss);
  }
  .back-brand__mark {
    display: inline-block; width: 26px; height: 26px; border-radius: 50%;
    background: var(--emboss); vertical-align: middle; margin-right: 14px;
  }
  .back-brand__name {
    font-weight: 700; font-size: 34px; letter-spacing: 2px;
    text-transform: uppercase; vertical-align: middle;
  }
  .back-tagline {
    margin-top: 26px; font-size: 19px; font-variant: small-caps;
    letter-spacing: 2px; font-weight: 600;
  }

  /* front */
  .front-panel {
    position: absolute; left: 0; top: 0; bottom: 0; width: 318px;
    background: var(--panel-light);
    padding: 70px 26px 0 30px;
    text-align: center;
  }
  .front-brand { display: flex; align-items: center; justify-content: center; gap: 12px; }
  .front-brand__mark { width: 34px; height: 34px; border-radius: 50%; background: var(--brand-blue); flex: none; }
  .front-brand__name {
    color: var(--brand-blue); font-weight: 700; font-size: 25px;
    line-height: 1.15; text-transform: uppercase; text-align: left; letter-spacing: 1px;
  }
  .front-tagline {
    margin-top: 28px; color: var(--ink); font-size: 17px;
    font-variant: small-caps; font-weight: 600; letter-spacing: 1px;
  }
  .front-claim {
    margin-top: 34px; color: var(--brand-blue); font-weight: 700;
    font-size: 17px; line-height: 1.3; text-transform: uppercase;
  }
  .ribbon { position: absolute; left: 0; top: 0; }
  .contact {
    position: absolute; left: 362px; right: 26px; top: 0;
    color: var(--white); font-size: 17px; line-height: 1.3;
  }
  .contact__row {
    border-bottom: 1.5px solid var(--white);
    display: flex; flex-direction: column; justify-content: center;
  }
  .contact__row:last-child { border-bottom: none; }
  .contact__row--name { height: 118px; padding-top: 34px; }
  .contact__row--phone { height: 72px; }
  .contact__row--web { height: 72px; }
  .contact__row--post { height: 88px; }
  .contact__name { color: var(--brand-blue); font-weight: 700; font-size: 22px; }
  .contact__role { font-size: 17px; }
</style>
</head>
<body>

<section class="card card--back" aria-label="Card back">
  <svg class="back-accents" width="700" height="400" viewBox="0 0 700 400">
    <polygon points="0,40 26,40 8,230 0,236" fill="var(--brand-blue)"/>
    <polygon points="700,150 700,372 676,372 688,162" fill="var(--brand-blue)"/>
  </svg>
  <div class="back-brand">
    <span class="back-brand__mark"></span><span class="back-brand__name">Keystone Floor Review</span>
    <p class="back-tagline">Analysis &amp; Consulting</p>
  </div>
</section>

<section class="card card--front" aria-label="Card front">
  <div class="front-panel">
    <div class="front-brand">
      <span class="front-brand__mark"></span>
      <span class="front-brand__name">Keystone<br>Floor Review</span>
    </div>
    <p class="front-tagline">Analysis &amp; Consulting</p>
    <p class="front-claim">Certified floor covering<br>inspections &amp; consulting</p>
  </div>

  <svg class="ribbon" width="362" height="400" viewBox="0 0 362 400">
    <polygon points="318,30 352,56 352,372 318,398 318,30" fill="var(--brand-blue)"/>
    <polygon points="318,30 352,56 318,56" fill="var(--brand-blue-deep)"/>
    <g stroke="var(--white)" stroke-width="1.5">
      <line x1="318" y1="118" x2="352" y2="118"/>
      <line x1="318" y1="190" x2="352" y2="190"/>
      <line x1="318" y1="262" x2="352" y2="262"/>
    </g>
    <!-- person -->
    <g fill="var(--white)">
      <circle cx="335" cy="80" r="5"/>
      <path d="M326 96 q0-9 9-9 q9 0 9 9 z"/>
    </g>
    <!-- phone -->
    <path d="M330 146 l4 -2 3 6 -3 2 q2 5 6 7 l2 -3 6 3 -2 4 q-11 0 -16 -17z" fill="var(--white)"/>
    <!-- globe -->
    <g fill="none" stroke="var(--white)" stroke-width="1.5">
      <circle cx="335" cy="226" r="9"/>
      <ellipse cx="335" cy="226" rx="4" ry="9"/>
      <line x1="326" y1="226" x2="344" y2="226"/>
    </g>
    <!-- pin -->
    <path d="M335 320 q-8 -9 -8 -14 a8 8 0 0 1 16 0 q0 5 -8 14z" fill="var(--white)"/>
    <circle cx="335" cy="306" r="3" fill="var(--brand-blue)"/>
  </svg>

  <div class="contact">
    <div class="contact__row contact__row--name">
      <span class="contact__name">Dana Marlowe</span>
      <span class="contact__role">Founder &amp; Owner</span>
    </div>
    <div class="contact__row contact__row--phone">
      <span>303.555.0142</span><span>888.555.0176</span>
    </div>
    <div class="contact__row contact__row--web">
      <span>dana@keystonefloorreview.com</span><span>www.keystonefloorreview.com</span>
    </div>
    <div class="contact__row contact__row--post">
      <span>P.O. Box 4417</span><span>Cedar Ridge, CO 80999</span>
    </div>
  </div>
</section>

</body>
</html>
```